Presentation Template for Copperline Ventures

We would like to have a template for our presentations since we have a new logo and want a new general image.

The new template should have as minimum Cover/Title Page, Bullets page and Regular page. We have a new logo and need the template to mach with it. For the bullets and regular page we want the design no take much part for including content, so we would like something that makes the slides look good but leaving most of room free for writing.

We would like the logo on the footer of the regular slides (not of course for the cover, dividers etc)

I'm attaching de logo here. Our logo colours are #b80016, #006ac6 and black

Thank you

Industry/Entity Type

It Company

Font styles to use
Other font styles liked:
• Maven Pro

Colors
ec1f27
0355a3
000000

Requirements
Must have
• Presentation template with Cover/Title Page, Bullets page and Regular page. Must match with our new logo.
• We would like the logo on the footer of the regular slides (not of course for the cover, dividers etc)
• Our logo colours are #b80016, #006ac6 and black
Nice to have
• Other type of slides, special bullets etc
Should not have
• I don't know

```html
<!DOCTYPE html>
<html lang="en">
<head>
<meta charset="utf-8">
<title>Copperline Ventures — Presentation Template</title>
<link href="https://fonts.googleapis.com/css2?family=Maven+Pro:wght@400;500;600;700&display=swap" rel="stylesheet">
<style>
:root{
  --red:#c8141e;
  --red-deep:#b80016;
  --blue:#0a63c9;
  --blue-deep:#0355a3;
  --black:#000;
  --ink:#1b1b1b;
  --grey:#9a9a9a;
  --line:#e3e3e3;
  --canvas:#d9dadc;
}
*{box-sizing:border-box;margin:0;padding:0}
html,body{width:1060px;height:1200px;overflow:hidden}
body{background:var(--canvas);font-family:"Maven Pro",Arial,sans-serif;color:var(--ink)}
.deck{position:absolute;left:6px;top:4px;display:grid;grid-template-columns:repeat(3,344px);grid-auto-rows:192px;gap:8px}
.slide{position:relative;background:#fff;overflow:hidden;box-shadow:0 1px 3px rgba(0,0,0,.18)}
.abs{position:absolute}
.slide-title{position:absolute;left:18px;top:16px;font-size:14.5px;font-weight:400;letter-spacing:.2px;color:var(--ink);text-transform:uppercase;white-space:nowrap}
.slide-title::after{content:"";position:absolute;left:0;bottom:-4px;width:24px;height:2px;background:var(--red)}
.fine{font-size:3.7px;line-height:1.4;color:var(--grey)}
.fine.light{color:rgba(255,255,255,.85)}
.label{font-size:5.2px;font-weight:600;color:var(--ink)}
.label.red{color:var(--red)}
.label.blue{color:var(--blue)}
.photo{position:absolute}
.footer{position:absolute;left:0;right:0;bottom:0;height:6px;background:var(--blue)}
.footer .pg{position:absolute;left:7px;top:1px;font-size:3.6px;color:#fff}
.footer .pg::after{content:"";position:absolute;left:9px;top:0;width:.6px;height:4px;background:#fff}
.footer .legal{position:absolute;left:24px;top:1.2px;font-size:3.4px;color:#fff}
.footer-brand{position:absolute;right:0;bottom:0;height:11px;width:64px;background:#fff;clip-path:polygon(9px 0,100% 0,100% 100%,0 100%);display:flex;align-items:center;gap:2px;padding-left:13px;font-size:4.6px;font-weight:700;color:var(--red);letter-spacing:.2px}
.footer-brand i{display:block;width:5px;height:5px;background:var(--red)}
.tile{position:absolute;width:66px;height:63px;color:#fff;text-align:center;padding:12px 6px 0}
.tile b{display:block;font-size:5.4px;font-weight:600;margin-bottom:2px}
.tile.blue{background:var(--blue)} .tile.red{background:var(--red)}
.icon{position:absolute;border-radius:50%;display:flex;align-items:center;justify-content:center}
.icon svg{display:block}
.ring{border:1.4px solid #333;background:#fff}
.ring.blue{border-color:var(--blue)} .ring.red{border-color:var(--red)}
.band{position:absolute;left:0;right:0}
.bar{position:absolute;bottom:52px;width:18px}
.bar span{position:absolute;top:-9px;left:-4px;right:-4px;text-align:center;font-size:6px}
.bar.red{background:var(--red)} .bar.red span{color:var(--red)}
.bar.blue{background:var(--blue)} .bar.blue span{color:var(--blue)}
.bubble{position:absolute;border-radius:50%;color:#fff;display:flex;align-items:center;justify-content:center;font-weight:500;border:2px solid rgba(255,255,255,.8)}
.price-card{position:absolute;background:#fff;box-shadow:0 1px 3px rgba(0,0,0,.15);text-align:center}
.price-head{color:#fff;display:flex;flex-direction:column;justify-content:center;align-items:center}
.price-head strong{font-weight:400;line-height:1}
.price-head small{font-size:3.6px;opacity:.85}
.price-row{font-size:3.6px;color:#888;height:15px;line-height:15px;border-bottom:.5px solid var(--line);margin:0 8px}
.data-table{position:absolute;left:24px;top:62px;width:297px;border-collapse:collapse;font-size:3.8px}
.data-table th{background:var(--blue);color:#fff;font-weight:400;height:7px}
.data-table td{height:8.3px;text-align:center;color:#555;border-bottom:.5px solid #d5dbe6}
.data-table td.key{background:var(--blue);color:#fff;text-align:left;padding-left:4px;border-bottom:.5px solid #5c92d6}
.data-table tr:nth-child(even) td:not(.key){background:#eef3fa}
.member-name{font-size:5.2px;color:var(--ink)}
.member-role{font-size:4px;color:var(--blue)}
.avatar{position:absolute;border-radius:50%;border:2px solid #fff;box-shadow:0 0 0 .6px #ccc}
.client-badge{position:absolute;background:#b9bcc0}
</style>
</head>
<body>
<main class="deck">

<!-- 1 Brand detailed -->
<section class="slide">
  <h2 class="slide-title">Brand Detailed</h2>
  <div class="photo" role="img" aria-label="City skyline photograph at sunset" style="left:22px;top:48px;width:142px;height:127px;background:linear-gradient(180deg,#d9c9ad 0%,#a89a86 45%,#5f5b57 100%)"></div>
  <div class="tile blue" style="left:189px;top:52px"><b>System</b><p class="fine light">Mauris quam dolor, cursus at porta et, luctus eget purus. Nunc tempor luctus interdum.</p></div>
  <div class="tile red" style="left:257px;top:52px"><b>Technology</b><p class="fine light">Mauris quam dolor, cursus at porta et, luctus eget purus. Nunc tempor luctus interdum.</p></div>
  <div class="tile red" style="left:189px;top:118px"><b>Leisure</b><p class="fine light">Mauris quam dolor, cursus at porta et, luctus eget purus. Nunc tempor luctus interdum.</p></div>
  <div class="tile blue" style="left:257px;top:118px"><b>Digital</b><p class="fine light">Mauris quam dolor, cursus at porta et, luctus eget purus. Nunc tempor luctus interdum.</p></div>
  <footer class="footer"><span class="pg">19</span><span class="legal">© 2017 Copperline Ventures. All rights reserved</span><span class="footer-brand"><i></i>COPPERLINE</span></footer>
</section>

<!-- 2 Product philosophy -->
<section class="slide">
  <h2 class="slide-title">Product Philosophy</h2>
  <svg class="abs" style="left:120px;top:52px" width="104" height="104" viewBox="0 0 104 104" aria-label="Donut chart">
    <g transform="rotate(-90 52 52)" fill="none" stroke-width="24">
      <circle cx="52" cy="52" r="35" stroke="var(--red)" stroke-dasharray="77 220"/>
      <circle cx="52" cy="52" r="35" stroke="#3a3a3a" stroke-dasharray="0 77 48 220"/>
      <circle cx="52" cy="52" r="35" stroke="var(--black)" stroke-dasharray="0 125 42 220"/>
      <circle cx="52" cy="52" r="35" stroke="var(--blue)" stroke-dasharray="0 167 53 220"/>
    </g>
    <circle cx="52" cy="52" r="22" fill="#fff"/>
    <text x="52" y="54" text-anchor="middle" font-size="5" font-weight="700" fill="#c8141e" font-family="Maven Pro, sans-serif">COPPERLINE</text>
    <g font-size="7" font-weight="600" fill="#fff" font-family="Maven Pro, sans-serif" text-anchor="middle">
      <text x="34" y="25">20%</text><text x="84" y="38">35%</text>
      <text x="25" y="82">30%</text><text x="75" y="88">40%</text>
    </g>
  </svg>
  <div class="icon" style="left:113px;top:51px;width:26px;height:26px;background:var(--blue)"><svg width="12" height="12" viewBox="0 0 12 12"><circle cx="6" cy="6" r="5" fill="none" stroke="#fff" stroke-width="1"/><path d="M1 6h10M6 1c-2 3-2 7 0 10M6 1c2 3 2 7 0 10" fill="none" stroke="#fff" stroke-width=".7"/></svg></div>
  <div class="icon" style="left:235px;top:51px;width:26px;height:26px;background:var(--red)"><svg width="12" height="12" viewBox="0 0 12 12"><circle cx="3" cy="3" r="2" fill="#fff"/><circle cx="9" cy="9" r="2" fill="#fff"/><circle cx="9" cy="3" r="1.5" fill="#fff"/><path d="M3 3l6 6M9 3L3 9" stroke="#fff" stroke-width=".8"/></svg></div>
  <div class="icon" style="left:113px;top:131px;width:26px;height:26px;background:var(--black)"><svg width="12" height="12" viewBox="0 0 12 12"><path d="M6 1a3.5 3.5 0 0 1 2 6.3V9H4V7.3A3.5 3.5 0 0 1 6 1z" fill="none" stroke="#fff" stroke-width=".9"/><path d="M4.5 10.5h3" stroke="#fff" stroke-width=".9"/></svg></div>
  <div class="icon" style="left:235px;top:131px;width:26px;height:26px;background:#333"><svg width="12" height="12" viewBox="0 0 12 12"><rect x="1" y="2" width="10" height="7" fill="none" stroke="#fff" stroke-width=".9"/><path d="M3 5h4M3 7h6M4 11h4" stroke="#fff" stroke-width=".8"/></svg></div>
  <div class="abs" style="left:40px;top:50px;width:68px;text-align:right"><p class="label blue">Secure</p><p class="fine">Nullam eu tempor purus. Nunc a leo magna, sit amet consequat risus.</p></div>
  <div class="abs" style="left:266px;top:50px;width:68px"><p class="label red">Well Organized</p><p class="fine">Nullam eu tempor purus. Nunc a leo magna, sit amet consequat risus.</p></div>
  <div class="abs" style="left:40px;top:129px;width:68px;text-align:right"><p class="label">Good Package</p><p class="fine">Nullam eu tempor purus. Nunc a leo magna, sit amet consequat risus.</p></div>
  <div class="abs" style="left:266px;top:129px;width:68px"><p class="label">Publication</p><p class="fine">Nullam eu tempor purus. Nunc a leo magna, sit amet consequat risus.</p></div>
  <p class="fine abs" style="left:30px;top:166px;width:290px;text-align:center">Lorem ipsum dolor sit amet, consectetur adipiscing elit. Sed at consectetur lacus. Sed sit amet nulla vel dolor gravida bibendum. Nunc odio massa, sodales et consectetur a, iaculis eget sapien. Mauris dignissim, arcu id facilisis laoreet.</p>
  <footer class="footer"><span class="pg">20</span><span class="legal">© 2017 Copperline Ventures. All rights reserved</span><span class="footer-brand"><i></i>COPPERLINE</span></footer>
</section>

<!-- 3 Bar chart -->
<section class="slide">
  <div class="photo" role="img" aria-label="Faded city skyline photograph" style="left:0;top:0;width:344px;height:140px;background:linear-gradient(180deg,#f4f5f7 0%,#e6e8ec 60%,#cfd3da 100%)"></div>
  <div class="abs" style="right:58px;top:9px;font-size:4.4px;display:flex;gap:4px"><span><i style="display:inline-block;width:4px;height:4px;background:var(--red)"></i> 2014</span><span><i style="display:inline-block;width:4px;height:4px;background:var(--blue)"></i> 2015</span></div>
  <div class="bar red" style="left:19px;height:55px"><span>400</span></div>
  <div class="bar blue" style="left:41px;height:69px"><span>500</span></div>
  <div class="bar red" style="left:98px;height:41px"><span>300</span></div>
  <div class="bar blue" style="left:120px;height:83px"><span>600</span></div>
  <div class="bar red" style="left:178px;height:40px"><span>290</span></div>
  <div class="bar blue" style="left:200px;height:28px"><span>200</span></div>
  <div class="bar red" style="left:257px;height:28px"><span>200</span></div>
  <div class="bar blue" style="left:279px;height:14px"><span>100</span></div>
  <div class="band" style="top:140px;height:46px;background:var(--blue)"></div>
  <div class="abs" style="left:8px;top:149px;width:328px;display:grid;grid-template-columns:repeat(4,1fr);gap:6px;text-align:center;color:#fff">
    <div><p style="font-size:5px;font-weight:600">Asia</p><p class="fine light">Duis quis purus adipiscing mi scelerisque dictum quis vel eros. Nullam eu tempor purus.</p></div>
    <div><p style="font-size:5px;font-weight:600">Africa</p><p class="fine light">Duis quis purus adipiscing mi scelerisque dictum quis vel eros. Nullam eu tempor purus.</p></div>
    <div><p style="font-size:5px;font-weight:600">America</p><p class="fine light">Duis quis purus adipiscing mi scelerisque dictum quis vel eros. Nullam eu tempor purus.</p></div>
    <div><p style="font-size:5px;font-weight:600">Euro</p><p class="fine light">Duis quis purus adipiscing mi scelerisque dictum quis vel eros. Nullam eu tempor purus.</p></div>
  </div>
  <footer class="footer"><span class="pg">21</span><span class="legal">© 2017 Copperline Ventures. All rights reserved</span><span class="footer-brand"><i></i>COPPERLINE</span></footer>
</section>

<!-- 4 Trending -->
<section class="slide">
  <h2 class="slide-title">Trending in the World</h2>
  <div class="photo" role="img" aria-label="Grey world map" style="left:18px;top:45px;width:218px;height:130px;border-radius:30px 40px 20px 50px;background:radial-gradient(ellipse at 50% 45%,#bdbdbd 0%,#c9c9c9 55%,#fff 72%)"></div>
  <div class="bubble" style="left:31px;top:98px;width:28px;height:28px;background:var(--blue);font-size:8px">25%</div>
  <div class="bubble" style="left:89px;top:80px;width:44px;height:44px;background:var(--red);font-size:12px">80%</div>
  <div class="bubble" style="left:187px;top:88px;width:40px;height:40px;background:var(--blue);font-size:11px">75%</div>
  <div class="bubble" style="left:160px;top:131px;width:25px;height:25px;background:#333;font-size:7px">15%</div>
  <div class="icon ring blue" style="left:244px;top:64px;width:20px;height:20px"><svg width="9" height="9" viewBox="0 0 10 10"><rect x="2" y="1" width="6" height="8" rx="1" fill="var(--blue)"/></svg></div>
  <div class="icon ring red" style="left:244px;top:100px;width:20px;height:20px"><svg width="9" height="9" viewBox="0 0 10 10"><path d="M3 9V4l1-3 1 3 1-3 1 3 1 1v5z" fill="var(--red)"/></svg></div>
  <div class="icon ring" style="left:244px;top:137px;width:20px;height:20px"><svg width="9" height="9" viewBox="0 0 10 10"><path d="M1 9h8M2 8V5M4 8V2M6 8V4M8 8V3" stroke="#333" stroke-width="1.2"/></svg></div>
  <div class="abs" style="left:270px;top:63px;width:66px"><p class="label blue">Confusion</p><p class="fine">Nullam eu tempor purus. Nunc a leo magna, sit amet consequat risus.</p></div>
  <div class="abs" style="left:270px;top:99px;width:66px"><p class="label red">Intangible</p><p class="fine">Nullam eu tempor purus. Nunc a leo magna, sit amet consequat risus.</p></div>
  <div class="abs" style="left:270px;top:136px;width:66px"><p class="label">Performance</p><p class="fine">Nullam eu tempor purus. Nunc a leo magna, sit amet consequat risus.</p></div>
  <footer class="footer"><span class="pg">22</span><span class="legal">© 2017 Copperline Ventures. All rights reserved</span><span class="footer-brand"><i></i>COPPERLINE</span></footer>
</section>

<!-- 5 Vision & Mission -->
<section class="slide">
  <h2 class="slide-title">Our Vision &amp; Mission</h2>
  <div class="photo" role="img" aria-label="Blue-toned city photograph" style="left:0;top:45px;width:344px;height:125px;background:linear-gradient(180deg,#1d6fd0 0%,#0a5bbd 55%,#0b4a9a 100%)"></div>
  <div class="abs" style="left:22px;top:66px;width:150px;color:#fff">
    <p style="font-size:8px">• Our Vision:</p>
    <p style="font-size:6.2px;font-weight:600;margin:5px 0 0 2px;line-height:1.5">Go to the Next Level<br>Without look in the past</p>
    <p class="fine light" style="margin:9px 0 0 2px">Lorem ipsum dolor sit amet, consectetur adipiscing elit, sed do eiusmod tempor incididunt ut labore et dolore magna aliqua. Ut enimad minim veniam, quis nostrud exercitation ullamco laboris nisi ut aliquip ex ea commodo consequat.</p>
  </div>
  <div class="abs" style="left:192px;top:66px;width:148px;color:#fff">
    <p style="font-size:8px">• Our Missions:</p>
    <div style="position:relative;margin-top:5px;padding-left:28px;height:26px"><span class="icon" style="left:6px;top:2px;width:15px;height:15px;background:rgba(255,255,255,.85)"></span><p style="font-size:8px">Your Text Here</p><p class="fine light">Lorem ipsum dolor sit amet consectetur adipiscing elit, sed do eiusmod tempo.</p></div>
    <div style="position:relative;padding-left:28px;height:26px"><span class="icon" style="left:6px;top:2px;width:15px;height:15px;background:rgba(255,255,255,.85)"></span><p style="font-size:8px">Your Text Here</p><p class="fine light">Lorem ipsum dolor sit amet consectetur adipiscing elit, sed do eiusmod tempo.</p></div>
    <div style="position:relative;padding-left:28px;height:26px"><span class="icon" style="left:6px;top:2px;width:15px;height:15px;background:rgba(255,255,255,.85)"></span><p style="font-size:8px">Your Text Here</p><p class="fine light">Lorem ipsum dolor sit amet consectetur adipiscing elit, sed do eiusmod tempo.</p></div>
  </div>
  <footer class="footer"><span class="pg">23</span><span class="legal">© 2017 Copperline Ventures. All rights reserved</span><span class="footer-brand"><i></i>COPPERLINE</span></footer>
</section>

<!-- 6 Services -->
<section class="slide">
  <h2 class="slide-title">Our Services</h2>
  <div class="photo" role="img" aria-label="Person seated in an old city street" style="left:32px;top:45px;width:134px;height:83px;background:linear-gradient(160deg,#b3a48b 0%,#7d705f 50%,#4a4540 100%)"></div>
  <div class="abs" style="left:32px;top:133px;width:134px"><p style="font-size:5px">Your Title Goes Here</p><p class="fine">Lorem ipsum dolor sit amet, consectetur adipiscing elit, sed do eiusmod tempor incididunt ut labore et dolore magna aliqua. Ut enim ad minim veniam, quis nostrud exercitation ullamco laboris nisi ut aliquip ex ea commodo consequat.</p></div>
  <div class="icon" style="left:190px;top:49px;width:13px;height:13px;background:var(--blue)"><svg width="6" height="6" viewBox="0 0 6 6"><path d="M1 5V3M3 5V1M5 5V2" stroke="#fff" stroke-width="1"/></svg></div>
  <div class="icon" style="left:190px;top:90px;width:13px;height:13px;background:var(--red)"><svg width="6" height="6" viewBox="0 0 6 6"><path d="M1 5l4-4M3 1h2v2" stroke="#fff" stroke-width="1" fill="none"/></svg></div>
  <div class="icon" style="left:190px;top:131px;width:13px;height:13px;background:var(--black)"><svg width="6" height="6" viewBox="0 0 6 6"><circle cx="2.5" cy="2.5" r="1.7" fill="none" stroke="#fff" stroke-width=".9"/><path d="M4 4l1.5 1.5" stroke="#fff" stroke-width=".9"/></svg></div>
  <div class="abs" style="left:210px;top:48px;width:128px"><p style="font-size:6px;color:var(--blue)">Service Number One</p><p class="fine">Lorem ipsum dolor sit amet, consectetur adipiscing elit, sed do eiusmod tempor incididunt ut labore et dolore magna aliqua.</p></div>
  <div class="abs" style="left:210px;top:89px;width:128px"><p style="font-size:6px;color:var(--red)">Service Number Two</p><p class="fine">Lorem ipsum dolor sit amet, consectetur adipiscing elit, sed do eiusmod tempor incididunt ut labore et dolore magna aliqua.</p></div>
  <div class="abs" style="left:210px;top:130px;width:128px"><p style="font-size:6px">Service Number Three</p><p class="fine">Lorem ipsum dolor sit amet, consectetur adipiscing elit, sed do eiusmod tempor incididunt ut labore et dolore magna aliqua.</p></div>
  <footer class="footer"><span class="pg">24</span><span class="legal">© 2017 Copperline Ventures. All rights reserved</span><span class="footer-brand"><i></i>COPPERLINE</span></footer>
</section>

<!-- 7 Three column -->
<section class="slide">
  <h2 class="slide-title">Three Column Description</h2>
  <p class="abs" style="left:19px;top:56px;width:280px;font-size:6.4px;line-height:1.45">This is place for your header text. Insert your text here, just replace this text with your own text</p>
  <div class="abs" style="left:19px;top:84px;width:312px;display:grid;grid-template-columns:repeat(3,1fr);gap:14px">
    <div class="fine" style="font-size:4.4px"><p>Lorem ipsum dolor sit amet, consectetur adipiscing elit, sed do eiusmod tempor incididunt ut labore et dolore magna aliqua. Ut enimad minim veniam, quis nostrud exercitation ullamco laboris nisi ut aliquip ex ea commodo consequat.</p><p style="margin-top:5px">Duis aute irure dolor in reprehenderit in voluptate velit esse cillum dolore eu fugiat nulla pariatur excepteur.</p></div>
    <div class="fine" style="font-size:4.4px"><p>Lorem ipsum dolor sit amet, consectetur adipiscing elit, sed do eiusmod tempor incididunt ut labore et dolore magna aliqua. Ut enimad minim veniam, quis nostrud exercitation ullamco laboris nisi ut aliquip ex ea commodo consequat.</p><p style="margin-top:5px">Duis aute irure dolor in reprehenderit in voluptate velit esse cillum dolore eu fugiat nulla pariatur excepteur.</p></div>
    <div class="fine" style="font-size:4.4px"><p>Lorem ipsum dolor sit amet, consectetur adipiscing elit, sed do eiusmod tempor incididunt ut labore et dolore magna aliqua. Ut enimad minim veniam, quis nostrud exercitation ullamco laboris nisi ut aliquip ex ea commodo consequat.</p><p style="margin-top:5px">Duis aute irure dolor in reprehenderit in voluptate velit esse cillum dolore eu fugiat nulla pariatur excepteur.</p></div>
  </div>
  <footer class="footer"><span class="pg">25</span><span class="legal">© 2017 Copperline Ventures. All rights reserved</span><span class="footer-brand"><i></i>COPPERLINE</span></footer>
</section>

<!-- 8 Our team single -->
<section class="slide">
  <h2 class="slide-title">Our Team</h2>
  <div class="avatar" role="img" aria-label="Portrait photograph of team member" style="left:132px;top:43px;width:80px;height:80px;background:radial-gradient(circle at 50% 40%,#d7c3b4 0%,#a99a90 55%,#6c7480 100%)"></div>
  <p class="abs" style="left:100px;top:131px;width:144px;text-align:center;font-size:4.4px">Mr JohnSmith</p>
  <p class="abs" style="left:100px;top:137px;width:144px;text-align:center;font-size:4.2px;color:var(--blue)">CEO</p>
  <p class="fine abs" style="left:112px;top:143px;width:120px;text-align:center">Lorem ipsum dolor sit amet, consectetur adipiscing elit, sed do eiusmod tempor incididunt ut labore et dolore magna aliqua. Duis aute irure dolor in reprehenderit in voluptate.</p>
  <div class="abs" style="left:160px;top:173px;display:flex;gap:2px"><i style="width:5px;height:5px;border-radius:50%;background:var(--blue)"></i><i style="width:5px;height:5px;border-radius:50%;background:var(--blue)"></i><i style="width:5px;height:5px;border-radius:50%;background:var(--blue)"></i><i style="width:5px;height:5px;border-radius:50%;background:var(--blue)"></i></div>
  <footer class="footer"><span class="pg">26</span><span class="legal">© 2017 Copperline Ventures. All rights reserved</span><span class="footer-brand"><i></i>COPPERLINE</span></footer>
</section>

<!-- 9 Clients -->
<section class="slide">
  <div class="client-badge" style="left:16px;top:20px;width:50px;height:22px"></div>
  <div class="client-badge" style="left:104px;top:16px;width:46px;height:30px;border-radius:4px"></div>
  <div class="client-badge" style="left:190px;top:18px;width:50px;height:26px"></div>
  <div class="client-badge" style="left:276px;top:22px;width:50px;height:18px;border-radius:2px"></div>
  <div class="client-badge" style="left:18px;top:84px;width:40px;height:30px;border-radius:50%"></div>
  <div class="client-badge" style="left:286px;top:86px;width:44px;height:26px;border-radius:13px"></div>
  <div class="client-badge" style="left:20px;top:140px;width:42px;height:32px;border-radius:50%"></div>
  <div class="client-badge" style="left:108px;top:136px;width:38px;height:38px;border-radius:50%"></div>
  <div class="client-badge" style="left:188px;top:140px;width:54px;height:32px"></div>
  <div class="client-badge" style="left:280px;top:140px;width:48px;height:32px"></div>
  <div class="abs" style="left:86px;top:66px;width:170px;height:62px;background:var(--blue);color:#fff;text-align:center;font-size:16.5px;line-height:1.4;padding-top:8px">OUR AWESOME<br>CLIENT</div>
  <footer class="footer"><span class="pg">27</span><span class="legal">© 2017 Copperline Ventures. All rights reserved</span><span class="footer-brand"><i></i>COPPERLINE</span></footer>
</section>

<!-- 10 Divider -->
<section class="slide" style="background:var(--red-deep)">
  <p class="abs" style="left:0;right:0;top:76px;text-align:center;color:#fff;font-size:16px;font-weight:700;letter-spacing:.4px">Copperline Ventures</p>
  <h2 class="abs" style="left:0;right:0;top:120px;text-align:center;color:#fff;font-size:13.5px;font-weight:700;letter-spacing:.5px">THIS IS YOUR DIVIDER PAGE</h2>
  <p class="abs" style="left:0;right:0;top:139px;text-align:center;color:#fff;font-size:5px">Subtitle Here</p>
  <p class="fine light abs" style="left:100px;top:147px;width:144px;text-align:center">Lorem ipsum dolor sit amet, consectetur adipiscing elit, sed do eiusmod tempor incididunt ut labore et dolore magna aliqua. Ut enimad minim veniam, quis nostrud exercitation ullamco laboris nisi ut aliquip ex ea commodo consequat.</p>
</section>

<!-- 11 Monthly subscription -->
<section class="slide">
  <h2 class="slide-title">Monthly Subscription</h2>
  <div class="band" style="top:97px;bottom:0;background:var(--blue)"></div>
  <div class="price-card" style="left:50px;top:65px;width:70px;height:106px">
    <div class="price-head" style="height:31px;background:var(--black)"><strong style="font-size:13px">$300</strong><small>per month</small></div>
    <div class="price-row">Single Edition</div><div class="price-row">30gb Cloud Service</div><div class="price-row">3 User</div><div class="price-row" style="border:0">Free Update</div>
  </div>
  <div class="price-card" style="left:128px;top:62px;width:88px;height:114px">
    <div class="price-head" style="height:34px;background:var(--blue)"><strong style="font-size:15px">$900</strong><small>per month</small></div>
    <div class="price-row" style="height:17px;line-height:17px">Business Edition</div><div class="price-row" style="height:17px;line-height:17px">60gb Cloud Service</div><div class="price-row" style="height:17px;line-height:17px">6 User</div><div class="price-row" style="border:0;height:17px;line-height:17px">Free Update</div>
  </div>
  <div class="price-card" style="left:224px;top:65px;width:70px;height:106px">
    <div class="price-head" style="height:31px;background:var(--red)"><strong style="font-size:13px">$400</strong><small>per month</small></div>
    <div class="price-row">Single Edition</div><div class="price-row">30gb Cloud Service</div><div class="price-row">3 User</div><div class="price-row" style="border:0">Free Update</div>
  </div>
</section>

<!-- 12 Table -->
<section class="slide">
  <h2 class="slide-title">Your Title Goes Here</h2>
  <p class="fine abs" style="left:24px;top:46px;width:300px"><span style="color:var(--blue)">Description</span> — There are many variations of passages of lorem ipsum available, but the majority have suffered alteration in some form, by injected humour, or randomised words which don't look even slightly believable.</p>
  <table class="data-table">
    <thead><tr><th style="text-align:left;padding-left:4px">Lorem ipsum</th><th>Value</th><th>Value</th><th>Value</th><th>Value</th></tr></thead>
    <tbody>
      <tr><td class="key">Lorem ipsum</td><td>10</td><td>15</td><td>16</td><td>18</td></tr>
      <tr><td class="key">Lorem ipsum</td><td>12</td><td>13</td><td>15</td><td>16</td></tr>
      <tr><td class="key">Lorem ipsum</td><td></td><td></td><td></td><td></td></tr>
      <tr><td class="key">Lorem ipsum</td><td>20</td><td>22</td><td>21</td><td>21</td></tr>
      <tr><td class="key">Lorem ipsum</td><td>10</td><td>21</td><td>12</td><td>11</td></tr>
      <tr><td class="key">Lorem ipsum</td><td>25</td><td>25</td><td>25</td><td>25</td></tr>
      <tr><td class="key">Lorem ipsum</td><td>10</td><td>02</td><td>51</td><td>21</td></tr>
      <tr><td class="key">Lorem ipsum</td><td>35</td><td>35</td><td>65</td><td>32</td></tr>
      <tr><td class="key">Lorem ipsum</td><td>26</td><td>33</td><td>35</td><td>32</td></tr>
      <tr><td class="key">Lorem ipsum</td><td>32</td><td>10</td><td>32</td><td>32</td></tr>
    </tbody>
  </table>
  <footer class="footer"><span class="pg">30</span><span class="legal">© 2017 Copperline Ventures. All rights reserved</span><span class="footer-brand"><i></i>COPPERLINE</span></footer>
</section>

<!-- 13 Our team four -->
<section class="slide">
  <h2 class="slide-title">Our Team</h2>
  <div class="avatar" role="img" aria-label="Portrait photograph of team member" style="left:20px;top:50px;width:34px;height:34px;background:radial-gradient(circle at 50% 40%,#cdb8a8,#7b7e86)"></div>
  <div class="abs" style="left:63px;top:53px;width:100px"><p class="member-name">Michael Doe</p><p class="member-role">CEO</p><p class="member-role" style="color:var(--red)">MSc, MBA and CIMA Dip PM</p><p class="fine">• Lorem ipsum dolor sit amet, consectetur adipiscing elit<br>• sed do eiusmod tempor incididunt ut labore et dolore magna aliqua<br>• Ut enimad minim veniam, quis nostrud</p></div>
  <div class="avatar" role="img" aria-label="Portrait photograph of team member" style="left:178px;top:50px;width:34px;height:34px;background:radial-gradient(circle at 50% 40%,#dcc5b3,#8d8f94)"></div>
  <div class="abs" style="left:221px;top:53px;width:100px"><p class="member-name">James Doe</p><p class="member-role">Manager</p><p class="member-role" style="color:var(--red)">M.B.A</p><p class="fine">• Lorem ipsum dolor sit amet, consectetur adipiscing elit<br>• sed do eiusmod tempor incididunt ut labore et dolore magna aliqua<br>• Ut enimad minim veniam, quis nostrud</p></div>
  <div class="avatar" role="img" aria-label="Portrait photograph of team member" style="left:20px;top:114px;width:34px;height:34px;background:radial-gradient(circle at 50% 40%,#e6d0bd,#b4a48f)"></div>
  <div class="abs" style="left:63px;top:117px;width:100px"><p class="member-name">Jane Doe</p><p class="member-role">Doctor of Chemistry</p><p class="member-role" style="color:var(--red)">M.B.A</p><p class="fine">• Lorem ipsum dolor sit amet, consectetur adipiscing elit<br>• sed do eiusmod tempor incididunt ut labore et dolore magna aliqua<br>• Ut enimad minim veniam, quis nostrud</p></div>
  <div class="avatar" role="img" aria-label="Portrait photograph of team member" style="left:178px;top:114px;width:34px;height:34px;background:radial-gradient(circle at 50% 40%,#d8bfae,#6f7884)"></div>
  <div class="abs" style="left:221px;top:117px;width:100px"><p class="member-name">John Doe</p><p class="member-role">Doctor of Physical</p><p class="member-role" style="color:var(--red)">Professor</p><p class="fine">• Lorem ipsum dolor sit amet, consectetur adipiscing elit<br>• sed do eiusmod tempor incididunt ut labore et dolore magna aliqua<br>• Ut enimad minim veniam, quis nostrud</p></div>
  <footer class="footer"><span class="pg">31</span><span class="legal">© 2017 Copperline Ventures. All rights reserved</span><span class="footer-brand"><i></i>COPPERLINE</span></footer>
</section>

<!-- 14 Testimonials -->
<section class="slide">
  <h2 class="slide-title">Customer Testimonials</h2>
  <div class="avatar" role="img" aria-label="Portrait photograph of customer" style="left:74px;top:42px;width:46px;height:46px;background:radial-gradient(circle at 50% 40%,#d0bba9,#717883)"></div>
  <p class="fine abs" style="left:150px;top:53px;width:160px;font-size:4.2px">adipiscing elit, sed diam nonummy nibh euismod tincidunt ut laoreet dolore magna aliquam erat volutpat. Ut wisi enim <b style="color:#555">Lorem ipsum</b> dolor sit amet, consectetuer adipiscing elit, sed diam nonummy nibh euismod tincidunt ut laoreet dolore magna.</p>
  <div class="band" style="top:102px;bottom:0;background:var(--blue)"></div>
  <svg class="abs" style="left:91px;top:97px" width="12" height="6" viewBox="0 0 12 6"><path d="M0 6L6 0l6 6z" fill="var(--blue)"/></svg>
  <div class="abs" style="left:40px;top:122px;width:264px;display:grid;grid-template-columns:repeat(4,1fr);gap:10px;text-align:center">
    <div><span class="icon" style="position:relative;margin:0 auto;width:24px;height:24px;border:1px solid #fff"></span><p class="fine light" style="margin-top:5px">Why does getting a loan have to be so much more complicated than ordering online?</p></div>
    <div><span class="icon" style="position:relative;margin:0 auto;width:24px;height:24px;border:1px solid #fff"></span><p class="fine light" style="margin-top:5px">Why do I have to go to a branch, fill out forms and wait for weeks for a reply?</p></div>
    <div><span class="icon" style="position:relative;margin:0 auto;width:24px;height:24px;border:1px solid #fff"></span><p class="fine light" style="margin-top:5px">Why do banks refuse to lend to me despite the substantial fees I receive each month?</p></div>
    <div><span class="icon" style="position:relative;margin:0 auto;width:24px;height:24px;border:1px solid #fff"></span><p class="fine light" style="margin-top:5px">Why is there no store in banking that simplifies my needs and offers fair prices?</p></div>
  </div>
</section>

<!-- 15 Two pictures -->
<section class="slide">
  <h2 class="slide-title">Two Pictures Slide</h2>
  <div class="photo" role="img" aria-label="Glass skyscrapers seen from below" style="left:26px;top:40px;width:145px;height:130px;background:linear-gradient(135deg,#2b3a4d 0%,#6f87a3 45%,#c6d2de 100%)"></div>
  <div class="photo" role="img" aria-label="Golden skyscrapers seen from below at sunset" style="left:176px;top:40px;width:145px;height:130px;background:linear-gradient(135deg,#3d3a33 0%,#9a8a66 45%,#ead9b2 100%)"></div>
  <footer class="footer"><span class="pg">33</span><span class="legal">© 2017 Copperline Ventures. All rights reserved</span><span class="footer-brand"><i></i>COPPERLINE</span></footer>
</section>

<!-- 16 Title and image + text -->
<section class="slide">
  <h2 class="slide-title">Title and Image + Text</h2>
  <div class="photo" role="img" aria-label="Black and white photograph of escalators" style="left:24px;top:38px;width:308px;height:72px;background:linear-gradient(160deg,#2a2a2a 0%,#8a8a8a 40%,#3a3a3a 70%,#b5b5b5 100%)"></div>
  <p class="abs" style="left:26px;top:120px;width:150px;font-size:7px;line-height:1.4">Lorem ipsum dolor sit amet, consectetur adipiscing elit, sed do eiusmod tempor incididunt ut labore et dolore magna aliqua. Ut enimad minim veniam, quis</p>
  <div class="abs" style="left:188px;top:120px;width:142px"><p class="fine">Lorem ipsum dolor sit amet, consectetur adipiscing elit, sed do eiusmod tempor incididunt ut labore et dolore magna aliqua. Ut enimad minim veniam, quis nostrud exercitation ullamco laboris nisi ut aliquip ex ea commodo consequat.</p><p class="fine" style="margin-top:5px">Duis aute irure dolor in reprehenderit in voluptate velit esse cillum dolore eu fugiat nulla pariatur. Excepteur sint occaecat cupidatat non proident, sunt in culpa qui officia deserunt mollit anim id est laborum.</p></div>
  <footer class="footer"><span class="pg">34</span><span class="legal">© 2017 Copperline Ventures. All rights reserved</span><span class="footer-brand"><i></i>COPPERLINE</span></footer>
</section>

<!-- 17 Three bullets -->
<section class="slide">
  <h2 class="slide-title">Three Bullets Area</h2>
  <div class="photo" role="img" aria-label="Black and white photograph of station escalators" style="left:0;top:38px;width:344px;height:76px;background:linear-gradient(180deg,#555 0%,#a9a9a9 45%,#6e6e6e 100%)"></div>
  <div class="icon" style="left:43px;top:105px;width:40px;height:40px;background:var(--blue);border:2px solid #fff"><svg width="16" height="16" viewBox="0 0 16 16"><circle cx="4" cy="8" r="2" fill="none" stroke="#fff" stroke-width="1.2"/><circle cx="12" cy="3.5" r="2" fill="none" stroke="#fff" stroke-width="1.2"/><circle cx="12" cy="12.5" r="2" fill="none" stroke="#fff" stroke-width="1.2"/><path d="M6 7l4-2.5M6 9l4 2.5" stroke="#fff" stroke-width="1.2"/></svg></div>
  <div class="icon" style="left:152px;top:105px;width:40px;height:40px;background:var(--red);border:2px solid #fff"><svg width="16" height="16" viewBox="0 0 16 16"><path d="M8 2l6 3-6 3-6-3z" fill="none" stroke="#fff" stroke-width="1.2"/><path d="M2 8l6 3 6-3M2 11l6 3 6-3" fill="none" stroke="#fff" stroke-width="1.2"/></svg></div>
  <div class="icon" style="left:262px;top:105px;width:40px;height:40px;background:var(--black);border:2px solid #fff"><svg width="16" height="16" viewBox="0 0 16 16"><path d="M5 14h7l-1-4 1-4-3-4-4 3 1 2 2-1z" fill="#fff"/></svg></div>
  <p class="fine abs" style="left:18px;top:150px;width:90px;text-align:center">Lorem ipsum dolor sit amet, consectetur adipiscing elit, sed do eiusmod tempor incididunt ut labore</p>
  <p class="fine abs" style="left:127px;top:150px;width:90px;text-align:center">Lorem ipsum dolor sit amet, consectetur adipiscing elit, sed do eiusmod tempor incididunt ut labore</p>
  <p class="fine abs" style="left:237px;top:150px;width:90px;text-align:center">Lorem ipsum dolor sit amet, consectetur adipiscing elit, sed do eiusmod tempor incididunt ut labore</p>
  <footer class="footer"><span class="pg">35</span><span class="legal">© 2017 Copperline Ventures. All rights reserved</span><span class="footer-brand"><i></i>COPPERLINE</span></footer>
</section>

<!-- 18 Thank you -->
<section class="slide" style="background:var(--blue)">
  <div class="photo" role="img" aria-label="Dark world map with glowing location points" style="left:0;top:0;width:344px;height:192px;clip-path:polygon(246px 0,344px 0,344px 192px,154px 192px);background:radial-gradient(circle at 75% 55%,#4d5562 0%,#262a31 45%,#101214 100%)"></div>
  <h2 class="abs" style="left:16px;top:15px;color:#fff;font-size:25px;font-weight:700;letter-spacing:1px">THANK YOU</h2>
  <p class="abs" style="left:17px;top:46px;color:#fff;font-size:11.5px;letter-spacing:.5px">SEND YOUR FEEDBACK</p>
  <ul class="abs" style="left:18px;top:76px;list-style:none;color:#fff;font-size:3.8px;line-height:1.3">
    <li style="display:flex;gap:5px;align-items:center;margin-bottom:6px"><svg width="6" height="6" viewBox="0 0 6 6"><path d="M0 3L3 0l3 3H5v3H1V3z" fill="#fff"/></svg><span>123 Street Road<br>City 12345</span></li>
    <li style="display:flex;gap:5px;align-items:center;margin-bottom:6px"><svg width="6" height="6" viewBox="0 0 6 6"><path d="M1 0h1.5l.5 1.5-1 .8a4 4 0 0 0 1.7 1.7l.8-1 1.5.5V5a1 1 0 0 1-1 1A5 5 0 0 1 0 1a1 1 0 0 1 1-1z" fill="#fff"/></svg><span>(123) 456-7890</span></li>
    <li style="display:flex;gap:5px;align-items:center;margin-bottom:6px"><svg width="6" height="6" viewBox="0 0 6 6"><rect y="1" width="6" height="4" fill="#fff"/><path d="M0 1l3 2 3-2" stroke="var(--blue)" stroke-width=".6" fill="none"/></svg><span>emailaddress@email.com</span></li>
    <li style="display:flex;gap:5px;align-items:center"><svg width="6" height="6" viewBox="0 0 6 6"><circle cx="3" cy="3" r="2.7" fill="#fff"/></svg><span>www.website-address.com</span></li>
  </ul>
  <div class="abs" style="left:16px;top:158px;display:flex;align-items:center;gap:3px;font-size:6px;font-weight:700;color:var(--red-deep)"><i style="display:block;width:7px;height:7px;background:var(--red-deep)"></i>COPPERLINE VENTURES</div>
</section>

</main>
</body>
</html>
```